Toms welding and seed cleaning Business cards

Toms welding and seed cleaningWe clean wheat seed on farm with portable cleaners so the farmers have pure wheat seed to plant back for the next crop. We are certified to clean foundation, registered, and certified seed wheat. Our cleaners being portable make it easier for the farmers because we do it right on there farm so they don't have to haul it all to townWhen there is no wheat to clean we weld in the winter. We improve, add onto, and build new corrals. We also build sheds, cattle shelters, and wind breaks. Other welding is welcomed
Updates

Project Deadline Extended
Reason: I need to extend the deadline because I've been busy and not had my game together. I need more time figure out what I want yet

Industry/Entity Type

Agriculture

Contact Information for Business Card

Just "toms welding and seed cleaning" on front and other info on the back
On the back side I would like to have my address.
Martin Bellard
48903 N COUNTY RD 137
GLENWOOD OK 73612
Phone #5804419163

Font styles to use
Sans Serif

Requirements
Must have
• list we are certified to clean foundation, registered, and certified wheat
• State that they are portable cleaners
• For the welding part list, add on to, improve on, and repair existing corrals and new corrals and other welding welcomed
Nice to have
• A wheat field with some metal corrals on the side with a nice classic looking barn for a background. Maybe some cattle in the corrals
• A nice looking farm yard would be good too

```html
<!DOCTYPE html>
<html lang="en">
<head>
<meta charset="utf-8">
<title>Toms Welding and Seed Cleaning – Business Card</title>
<link rel="stylesheet" href="https://fonts.googleapis.com/css2?family=Bebas+Neue&family=Jost:wght@400&display=swap">
<style>
  :root {
    --page: #f2f2f2;
    --card: #ffffff;
    --sky: #9fb6a0;
    --sky-deep: #7e9888;
    --wheat-light: #e6b24a;
    --wheat: #c98a1e;
    --wheat-deep: #8a5a14;
    --disc: rgba(255, 255, 255, 0.82);
    --name-brown: #9a5640;
    --gold-text: #c0862c;
    --sage: #8aa184;
    --rule: #d9b67a;
  }
  * { box-sizing: border-box; margin: 0; padding: 0; }
  html, body {
    width: 1200px;
    height: 900px;
    overflow: hidden;
    background: var(--page);
  }
  .sheet {
    width: 1200px;
    height: 900px;
    display: flex;
    flex-direction: column;
    align-items: center;
    justify-content: center;
    gap: 40px;
  }
  .card {
    position: relative;
    width: 700px;
    height: 400px;
    background: var(--card);
    overflow: hidden;
    box-shadow: 0 6px 18px rgba(0, 0, 0, 0.12);
  }
  .wheat-photo {
    position: absolute;
    background:
      linear-gradient(180deg,
        var(--sky-deep) 0%,
        var(--sky) 30%,
        var(--wheat-light) 55%,
        var(--wheat) 75%,
        var(--wheat-deep) 100%);
  }
  .card-front .wheat-photo { inset: 0; }
  .name-disc {
    position: absolute;
    border-radius: 50%;
    background: var(--disc);
    display: flex;
    align-items: center;
    justify-content: center;
    text-align: center;
    font-family: "Jost", sans-serif;
    font-weight: 400;
    color: var(--name-brown);
  }
  .card-front .name-disc {
    width: 300px;
    height: 300px;
    left: 200px;
    top: 50px;
    font-size: 28px;
    line-height: 1.3;
    padding: 0 30px;
  }
  .card-back .wheat-photo {
    width: 560px;
    height: 560px;
    left: -240px;
    top: -40px;
    border-radius: 50%;
  }
  .card-back .name-disc {
    width: 230px;
    height: 230px;
    left: 30px;
    top: 130px;
    font-size: 22px;
    line-height: 1.3;
    padding: 0 24px;
  }
  .service-info {
    position: absolute;
    right: 40px;
    top: 40px;
    width: 300px;
    text-align: right;
    font-family: "Jost", sans-serif;
    color: var(--gold-text);
  }
  .certification {
    font-size: 19px;
    line-height: 1.25;
  }
  .divider {
    height: 1px;
    background: var(--rule);
    margin: 16px 0;
  }
  .portable-title {
    font-family: "Bebas Neue", sans-serif;
    font-weight: 400;
    font-size: 54px;
    line-height: 0.9;
    color: var(--sage);
    letter-spacing: 1px;
  }
  .welding-services {
    font-size: 17px;
    line-height: 1.3;
  }
</style>
</head>
<body>
  <main class="sheet">
    <section class="card card-front">
      <div class="wheat-photo" role="img" aria-label="Golden wheat field under a soft green sky"></div>
      <h1 class="name-disc">Toms Welding and Seed Cleaning</h1>
    </section>

    <section class="card card-back">
      <div class="wheat-photo" role="img" aria-label="Golden wheat field under a soft green sky"></div>
      <p class="name-disc">Toms Welding and Seed Cleaning</p>
      <div class="service-info">
        <p class="certification">Certified to:<br>Clean foundation, Registered,<br>and Certified wheat</p>
        <div class="divider"></div>
        <h2 class="portable-title">Portable<br>Cleaners</h2>
        <div class="divider"></div>
        <p class="welding-services">Build, improve, add on to, and repair<br>existing and new corrals.<br>Other welding welcomed</p>
      </div>
    </section>
  </main>
</body>
</html>
```